Ad Template Needed for Postboardia PLEASE!

Hi, I need a professional designer who can design a template for real estate ads for Postboardia.
The ads I am currently running are OK, but I need them to have a bit more of a professional polish.
Here is what I need:
The ads must direct people to click my "questionnaire", this is a short survey that is completed off site.
The ads should also entice the viewer to contact me thought email or phone.
PLEASE NO COOKIE-CUTTER ADS!. No stock photos, or generic content. These must be original.
I have attached the html for my previous ads. Please provide previous work if you apply for the job.
Here are links to some the actual ads I am currently running, these are a good base, but I need them to be improved. You would be redesigning these:
http://newyork.postboardia.example/mnh/nfb/3474576998.html
http://newyork.postboardia.example/mnh/nfb/3474576813.html
http://newyork.postboardia.example/mnh/nfb/3474547558.html
http://newyork.postboardia.example/mnh/nfb/3474518339.html
IMPORTANT PLEASE READ:
You will not have to do anything with the photos in the ads, I can change these out as needed.
You do not need to worry about content, meaning wording.
These ads MUST be full width.
I will need these coded to HTML, not sure if that is feasible with my budget, it not please let me know.
Let me know if you have any questions, thank you.
Real Estate

```html
<!DOCTYPE html>
<html lang="en">
<head>
<meta charset="utf-8">
<title>Varden Properties – Listing Ad</title>
<link href="https://fonts.googleapis.com/css2?family=Arimo:wght@400;700&family=Roboto:wght@300;400;700&display=swap" rel="stylesheet">
<style>
  :root {
    --brand-red: #c8120f;
    --deep-red: #a50d0d;
    --ribbon-red: #cc4747;
    --ribbon-dark: #9e2f2f;
    --ink: #111111;
    --muted-ink: #333333;
    --link-blue: #2f55d4;
    --band-grey: #f3f3f3;
    --panel-grey: #f7f7f7;
    --footer-grey: #e6e6e6;
    --rule-grey: #d4d4d4;
    --pill-blue: #d8e7f3;
    --white: #ffffff;
  }
  * { box-sizing: border-box; margin: 0; padding: 0; }
  html, body { width: 1029px; height: 1200px; overflow: hidden; background: var(--white); }
  body { position: relative; font-family: "Arimo", Arial, sans-serif; color: var(--ink); }
  .abs { position: absolute; }

  .top-rule { left: 86px; top: 3px; width: 857px; height: 3px; background: var(--rule-grey); }

  .brand { left: 0; top: 22px; width: 1029px; text-align: center; }
  .brand-name { font-family: "Arimo", Arial, sans-serif; font-weight: 400; color: var(--deep-red);
    font-size: 34px; letter-spacing: 8px; line-height: 1.1; }
  .brand-name span { display: block; }
  .brand-name .sub { font-size: 19px; letter-spacing: 13px; margin-top: 6px; }

  .agent-band { left: 0; top: 110px; width: 1029px; height: 196px; background: var(--band-grey);
    border-top: 1px solid var(--rule-grey); border-bottom: 1px solid var(--rule-grey); }
  .agent-card-panel { left: 480px; top: 130px; width: 262px; height: 162px; background: var(--panel-grey); }
  .agent-name-box { left: 480px; top: 130px; width: 262px; height: 54px; background: var(--white); }
  .agent-name { left: 480px; top: 143px; width: 245px; text-align: right; font-weight: 700;
    font-size: 27px; color: var(--brand-red); letter-spacing: 0.2px; }
  .agent-photo { left: 307px; top: 124px; width: 174px; height: 174px; border-radius: 50%;
    border: 1px solid var(--brand-red);
    background: radial-gradient(circle at 50% 38%, #e9d2c4 0%, #d9b9a6 28%, #f4f4f4 52%, #2c2c2c 90%); }
  .phone-icon { left: 513px; top: 206px; }
  .agent-phone { left: 538px; top: 203px; font-size: 22px; font-weight: 400; color: var(--ink); }
  .phone-rule { left: 512px; top: 236px; width: 167px; height: 1px; background: var(--ink); }
  .agent-title { left: 480px; top: 249px; width: 230px; text-align: center; font-weight: 700;
    font-size: 11px; letter-spacing: 1px; color: var(--ink); }

  .email-icon { left: 388px; top: 320px; }
  .agent-email { left: 425px; top: 315px; font-size: 19px; color: var(--link-blue); letter-spacing: 0.3px; }
  .email-rule { left: 0; top: 351px; width: 1029px; height: 1px; background: var(--rule-grey); }

  .listing-kicker { left: 0; top: 376px; width: 1029px; text-align: center; font-weight: 700;
    font-size: 11.5px; letter-spacing: 0.5px; }
  .listing-headline { left: 209px; top: 411px; font-weight: 700; font-size: 15px; }
  .listing-body { left: 209px; top: 437px; width: 620px; font-family: "Roboto", Arial, sans-serif;
    font-weight: 300; font-size: 11.5px; line-height: 20.5px; color: var(--ink); }
  .listing-body strong { font-weight: 700; }
  .agent-credit { left: 0; top: 503px; width: 1029px; text-align: center; font-family: "Roboto", Arial, sans-serif;
    font-size: 10.5px; color: var(--deep-red); }
  .listing-photo { left: 202px; top: 527px; width: 607px; height: 404px;
    background: linear-gradient(180deg, #e4e0da 0%, #dcdcdf 40%, #b9c2c9 62%, #7e7a76 78%, #d8d5d1 100%); }

  .alt-prompt { left: 0; top: 962px; width: 1029px; text-align: center; font-weight: 700; font-size: 15px; }
  .questionnaire-pill { left: 288px; top: 994px; width: 454px; height: 53px; border-radius: 27px;
    background: var(--pill-blue); }
  .question-icon { left: 306px; top: 1000px; }
  .questionnaire-text { left: 357px; top: 1011px; font-weight: 700; font-size: 15px; color: var(--ink); }
  .questionnaire-text .link { color: var(--link-blue); font-weight: 400; }

  .footer-panel { left: 113px; top: 1076px; width: 803px; height: 124px; background: var(--footer-grey);
    border-top: 4px solid var(--rule-grey); }
  .ribbon { left: 69px; top: 1085px; }
  .ribbon-label { left: 0; top: 1099px; width: 1029px; text-align: center; color: var(--white);
    font-weight: 700; font-size: 15.5px; letter-spacing: 0.6px; text-shadow: 0 1px 1px rgba(0,0,0,0.25); }
  .copyright { left: 0; top: 1155px; width: 1029px; text-align: center; font-size: 9px; color: var(--ink); }
</style>
</head>
<body>
  <div class="abs top-rule"></div>

  <header class="abs brand">
    <div class="brand-name"><span>varden</span><span class="sub">PROPERTIES</span></div>
  </header>

  <section class="agent">
    <div class="abs agent-band"></div>
    <div class="abs agent-card-panel"></div>
    <div class="abs agent-name-box"></div>
    <div class="abs agent-name">LUKE HARROW</div>
    <div class="abs agent-photo" role="img" aria-label="Agent headshot portrait"></div>
    <svg class="abs phone-icon" width="16" height="24" viewBox="0 0 16 24" aria-hidden="true">
      <rect x="1" y="1" width="14" height="22" rx="1.5" fill="var(--deep-red)"/>
      <rect x="3.5" y="3.5" width="9" height="7" fill="#f7f7f7"/>
      <g fill="#f7f7f7">
        <rect x="4" y="13" width="2" height="2"/><rect x="7" y="13" width="2" height="2"/><rect x="10" y="13" width="2" height="2"/>
        <rect x="4" y="16.5" width="2" height="2"/><rect x="7" y="16.5" width="2" height="2"/><rect x="10" y="16.5" width="2" height="2"/>
      </g>
    </svg>
    <div class="abs agent-phone">347-555-0142</div>
    <div class="abs phone-rule"></div>
    <div class="abs agent-title">YOUR FIDI SPECIALIST</div>
  </section>

  <section class="contact">
    <svg class="abs email-icon" width="24" height="16" viewBox="0 0 24 16" aria-hidden="true">
      <rect x="0" y="0" width="24" height="16" fill="var(--deep-red)"/>
      <polyline points="0,1 12,9 24,1" fill="none" stroke="#ffffff" stroke-width="1.4"/>
      <polyline points="0,16 9,7" stroke="#ffffff" stroke-width="1"/>
      <polyline points="24,16 15,7" stroke="#ffffff" stroke-width="1"/>
    </svg>
    <div class="abs agent-email">lukeh@vardenproperties.example</div>
    <div class="abs email-rule"></div>
  </section>

  <section class="listing">
    <div class="abs listing-kicker">~BRAND NEW TO MARKET~</div>
    <h1 class="abs listing-headline">Stunning Fi-Di Luxury Building!</h1>
    <p class="abs listing-body">This apartment has <strong>great light, space, and storage</strong>. Enjoy free amenities in a full service doorman building.<br>The unit comes with brand new stainless steel appliances and a 1 year old renovated kitchen and bathroom.</p>
    <div class="abs agent-credit">Luke Harrow | Licensed Salesperson | Varden Properties (347) 555-0142</div>
    <div class="abs listing-photo" role="img" aria-label="Living room with sofa and floor-to-ceiling windows overlooking the river"></div>
  </section>

  <section class="cta">
    <div class="abs alt-prompt">Looking for something else? No Problem.</div>
    <div class="abs questionnaire-pill"></div>
    <svg class="abs question-icon" width="40" height="42" viewBox="0 0 40 42" aria-hidden="true">
      <circle cx="20" cy="20" r="17" fill="var(--deep-red)" stroke="#ffffff" stroke-width="2"/>
      <path d="M14 33 L12 40 L20 35 Z" fill="var(--deep-red)"/>
      <text x="20" y="27" text-anchor="middle" font-family="Arimo, Arial, sans-serif" font-weight="700" font-size="20" fill="#ffffff">?</text>
    </svg>
    <div class="abs questionnaire-text"><span class="link">Click here</span> to Fill out my 60 second Questionnaire</div>
  </section>

  <footer>
    <div class="abs footer-panel"></div>
    <svg class="abs ribbon" width="891" height="62" viewBox="0 0 891 62" aria-hidden="true">
      <polygon points="0,14 44,14 44,61 0,61 12,37" fill="var(--ribbon-red)"/>
      <polygon points="891,14 847,14 847,61 891,61 879,37" fill="var(--ribbon-red)"/>
      <polygon points="27,45 44,61 44,45" fill="var(--ribbon-dark)"/>
      <polygon points="864,45 847,61 847,45" fill="var(--ribbon-dark)"/>
      <rect x="27" y="0" width="837" height="46" fill="var(--ribbon-red)"/>
      <line x1="29" y1="4" x2="862" y2="4" stroke="#ffffff" stroke-opacity="0.6" stroke-dasharray="2 2"/>
      <line x1="29" y1="42" x2="862" y2="42" stroke="#ffffff" stroke-opacity="0.6" stroke-dasharray="2 2"/>
      <line x1="3" y1="18" x2="44" y2="18" stroke="#ffffff" stroke-opacity="0.5" stroke-dasharray="2 2"/>
      <line x1="3" y1="57" x2="44" y2="57" stroke="#ffffff" stroke-opacity="0.5" stroke-dasharray="2 2"/>
      <line x1="847" y1="18" x2="888" y2="18" stroke="#ffffff" stroke-opacity="0.5" stroke-dasharray="2 2"/>
      <line x1="847" y1="57" x2="888" y2="57" stroke="#ffffff" stroke-opacity="0.5" stroke-dasharray="2 2"/>
    </svg>
    <div class="abs ribbon-label">SEE MY OTHER LISTINGS</div>
    <div class="abs copyright">© 2012 Varden Properties</div>
  </footer>
</body>
</html>
```